Marketing Flyer for churches and schools

We need a marketing flyer design for ongoing marketing activities. We are a bounce house and inflatable slide rental company. This flyer would be sent to churches schools and other non profits. We would like to create a set background for our flyer and then be able to edit the body of the text as we see fit. This will allow us to use this design for marketing throughout the year.

Target Market(s)

Schools and Churches

Requirements
Must have
• create flyer background with editable text fields that we can modify as we see fit. Should fit on letter size paper.
Nice to have
• A brochure style option along with the flyer.
Should not have
• N/A

```html
<!DOCTYPE html>
<html lang="en">
<head>
<meta charset="utf-8">
<title>Bounce House Rental Flyer</title>
<link rel="stylesheet" href="https://fonts.googleapis.com/css2?family=PT+Serif:wght@400;700&family=Open+Sans:wght@400;600;700&display=swap">
<style>
  :root {
    --stage: #4a4a4a;
    --paper: #ffffff;
    --red: #d9302a;
    --red-dark: #b8221d;
    --orange: #f28c1e;
    --blue: #1e9fd9;
    --blue-dark: #1a7fc0;
    --ink: #1b1b1b;
    --grey-text: #444444;
  }
  * { box-sizing: border-box; margin: 0; padding: 0; }
  html, body { width: 1200px; height: 857px; overflow: hidden; }
  body { background: var(--stage); position: relative; font-family: "Open Sans", sans-serif; }

  .flyer {
    position: absolute; left: 290px; top: 28px;
    width: 620px; height: 800px;
    background: var(--paper);
    overflow: hidden;
    box-shadow: 0 6px 24px rgba(0,0,0,.45);
  }
  .flyer__shapes { position: absolute; inset: 0; width: 620px; height: 800px; }

  .brand-badge {
    position: absolute; left: 445px; top: 283px; width: 170px; height: 170px;
    display: flex; align-items: center; justify-content: center; text-align: center;
    font-family: "PT Serif", serif; font-weight: 700; font-size: 30px; line-height: 1.05;
    color: var(--blue-dark);
  }

  .intro-copy {
    position: absolute; left: 375px; top: 512px; width: 192px;
    font-size: 10.5px; line-height: 1.35; color: var(--grey-text); text-align: right;
  }

  .headline {
    position: absolute; right: 26px; top: 606px; text-align: right;
    font-family: "PT Serif", serif; font-weight: 700; line-height: 1.12;
  }
  .headline__lead { display: block; font-size: 38px; color: var(--ink); }
  .headline__tail { display: block; font-size: 39px; color: var(--blue-dark); font-weight: 400; }

  .contact-bar {
    position: absolute; left: 0; bottom: 0; width: 620px; height: 76px;
    display: flex; align-items: center; padding: 0 24px; color: #fff;
  }
  .contact-bar__call { width: 178px; }
  .call-tag {
    display: inline-block; background: var(--orange); color: var(--red-dark);
    font-family: "PT Serif", serif; font-size: 13px; font-weight: 700;
    padding: 1px 10px; margin-bottom: 4px;
  }
  .call-number { font-family: "PT Serif", serif; font-size: 23px; font-weight: 700; line-height: 1.1; }
  .contact-bar__divider { width: 1px; height: 50px; background: rgba(255,255,255,.6); margin: 0 14px 0 4px; }
  .contact-bar__details { font-family: "PT Serif", serif; font-size: 12.5px; line-height: 1.9; }
  .contact-bar__label { font-size: 10px; letter-spacing: .5px; margin-right: 6px; }
</style>
</head>
<body>
  <article class="flyer">
    <svg class="flyer__shapes" viewBox="0 0 620 800">
      <defs>
        <linearGradient id="photo-tone" x1="0" y1="0" x2="0.25" y2="1">
          <stop offset="0" stop-color="#2f5a1e"/>
          <stop offset=".28" stop-color="#6f9a3a"/>
          <stop offset=".48" stop-color="#c9d98a"/>
          <stop offset=".7" stop-color="#6aa432"/>
          <stop offset="1" stop-color="#3d7a1e"/>
        </linearGradient>
        <linearGradient id="slide-blue" x1="0" y1="0" x2="0" y2="1">
          <stop offset="0" stop-color="#e8eef5"/>
          <stop offset="1" stop-color="#2b6fc4"/>
        </linearGradient>
        <linearGradient id="slide-multi" x1="0" y1="0" x2="1" y2="1">
          <stop offset="0" stop-color="#f0f3e6"/>
          <stop offset=".6" stop-color="#e2703a"/>
          <stop offset="1" stop-color="#5aa642"/>
        </linearGradient>
      </defs>

      <polygon points="0,0 620,0 620,338 0,490" fill="url(#photo-tone)" role="img" aria-label="Photo of three smiling children lying on the grass in a sunny park"/>

      <polygon points="413,0 455,0 620,165 620,218" fill="var(--blue)"/>
      <polygon points="455,0 478,0 620,142 620,165" fill="var(--paper)"/>
      <polygon points="478,0 518,0 620,102 620,142" fill="var(--red)"/>
      <polygon points="518,0 538,0 620,82 620,102" fill="var(--paper)"/>
      <polygon points="538,0 570,0 620,50 620,82" fill="var(--orange)"/>
      <polygon points="570,0 620,0 620,50" fill="var(--blue)"/>

      <polygon points="0,490 620,338 620,349 0,501" fill="var(--orange)"/>
      <polygon points="0,501 620,349 620,359 0,511" fill="var(--paper)"/>
      <polygon points="0,511 620,359 620,385 0,542" fill="var(--red)"/>
      <polygon points="0,552 330,470 330,478 0,562" fill="var(--blue)"/>

      <circle cx="112" cy="478" r="70" fill="var(--paper)" stroke="var(--blue)" stroke-width="5"/>
      <circle cx="112" cy="478" r="61" fill="url(#slide-blue)" role="img" aria-label="Blue inflatable water slide"/>
      <circle cx="300" cy="450" r="70" fill="var(--paper)" stroke="var(--red)" stroke-width="5"/>
      <circle cx="300" cy="450" r="61" fill="url(#slide-multi)" role="img" aria-label="Colourful inflatable dry slide"/>

      <circle cx="530" cy="368" r="82" fill="var(--paper)" stroke="var(--orange)" stroke-width="8"/>

      <rect x="0" y="718" width="620" height="6" fill="var(--blue)"/>
      <rect x="0" y="724" width="620" height="76" fill="var(--red)"/>
    </svg>

    <div class="brand-badge">Brazos<br>Hop</div>

    <p class="intro-copy">Keep your next school carnival, church picnic or fundraiser bouncing. We deliver, set up and clean every inflatable, with special rates for non-profits all year long.</p>

    <h1 class="headline">
      <span class="headline__lead">A bounce house and</span>
      <span class="headline__tail">inflatable slide rental company</span>
    </h1>

    <footer class="contact-bar">
      <div class="contact-bar__call">
        <span class="call-tag">CALL US:</span>
        <div class="call-number">(555) 214-0397</div>
      </div>
      <div class="contact-bar__divider"></div>
      <div class="contact-bar__details">
        <div><span class="contact-bar__label">ADDRESS:</span>1820 Maple Run Dr, Bryan Valley, TX 77000</div>
        <div><span class="contact-bar__label">WEBSITE:</span>www.hopzone-rentals.com</div>
      </div>
    </footer>
  </article>
</body>
</html>
```